Course Graduation Certificate

This project is not for a flyer but instead for the creation of a course graduation certificate. The final certificate needs to include the Marlowe Summit Aviation Academy logo and the text stating as follows:
Certifies that ___________________________ has satisfactorily completed the course of _______________________________ on ________________________________
I would also like to include some type of gold seal of completion as well as a place to sign my name and credentials at the bottom of the certificate
I have included the Marlowe Summit Aviation Academy logo as well as three other certificate examples for you to work from.
Target Market(s)
Students completing a certification course and receiving a certificate
Look and feel

```html
<!DOCTYPE html>
<html lang="en">
<head>
<meta charset="utf-8">
<title>Course Graduation Certificate – Marlowe Summit Aviation Academy</title>
<link rel="stylesheet" href="https://fonts.googleapis.com/css2?family=Montserrat:wght@500;600;700&display=swap">
<style>
  :root {
    --page: #ffffff;
    --paper: #eaf3fa;
    --cobalt: #1f62ae;
    --cobalt-soft: #6f9fd2;
    --ink: #222428;
    --rule: #7a7f86;
    --gold-light: #ffe27a;
    --gold: #e2ab1c;
    --gold-deep: #b07a0c;
  }
  * { box-sizing: border-box; margin: 0; padding: 0; }
  html, body {
    width: 1200px; height: 960px; overflow: hidden;
    background: var(--page);
    font-family: "Montserrat", sans-serif;
    color: var(--ink);
  }
  .certificate {
    position: absolute; left: 109px; top: 79px;
    width: 977px; height: 757px;
    background: var(--paper);
    box-shadow: 0 8px 18px rgba(0,0,0,0.28);
    overflow: hidden;
  }
  .header-artwork {
    position: absolute; left: 0; top: 0; width: 100%; height: 190px;
    background: linear-gradient(180deg, var(--cobalt) 0%, var(--cobalt) 45%, var(--cobalt-soft) 80%, var(--paper) 100%);
  }
  .footer-band {
    position: absolute; left: 0; bottom: 0; width: 100%; height: 51px;
    background: var(--cobalt);
  }
  .academy-title {
    position: absolute; top: 222px; left: 0; width: 100%;
    text-align: center; font-size: 21px; font-weight: 500; letter-spacing: 0.3px;
  }
  .statement { position: absolute; font-size: 22px; font-weight: 500; white-space: nowrap; }
  .statement--certifies { left: 203px; top: 296px; }
  .statement--completed { left: 0; width: 100%; text-align: center; top: 374px; }
  .statement--on { left: 600px; top: 456px; }
  .fill-line { position: absolute; height: 0; border-top: 1px solid var(--rule); }
  .fill-line--name { left: 354px; width: 420px; top: 318px; }
  .fill-line--course { left: 106px; width: 483px; top: 477px; }
  .fill-line--date { left: 637px; width: 225px; top: 477px; }
  .fill-line--signature { left: 375px; width: 227px; top: 555px; }
  .signatory-label {
    position: absolute; left: 375px; width: 227px; top: 566px;
    text-align: center; font-size: 16px; font-weight: 500;
  }
  .completion-seal {
    position: absolute; left: 63px; top: 533px; width: 152px; height: 152px;
    border-radius: 50%;
    background: radial-gradient(circle at 40% 35%, var(--gold-light) 0%, var(--gold) 55%, var(--gold-deep) 100%);
  }
  .academy-mark {
    position: absolute; left: 346px; top: 626px; width: 290px;
    text-align: center; font-size: 17px; font-weight: 700; line-height: 1.25;
    color: var(--cobalt); text-transform: uppercase;
  }
</style>
</head>
<body>
  <main class="certificate">
    <div class="header-artwork" role="img" aria-label="Decorative blue header with flowing sky lines and birds"></div>

    <h1 class="academy-title">MARLOWE SUMMIT AVIATION ACADEMY</h1>

    <p class="statement statement--certifies">Certifies that</p>
    <span class="fill-line fill-line--name"></span>

    <p class="statement statement--completed">has satisfactorily completed the course of</p>

    <span class="fill-line fill-line--course"></span>
    <p class="statement statement--on">on</p>
    <span class="fill-line fill-line--date"></span>

    <span class="fill-line fill-line--signature"></span>
    <p class="signatory-label">Authorised Signatory</p>

    <div class="completion-seal" role="img" aria-label="Gold seal of completion"></div>

    <p class="academy-mark">Marlowe Summit<br>Aviation Academy</p>

    <div class="footer-band"></div>
  </main>
</body>
</html>
```